New Years Greeting Card Design Competition

We need a greeting card design for the new year 2014. We would like to have pictures of our daughter Meera on the card. Please find attached 5 photos of her. Please feel free to use all 5 or some of them for the design. We would like the following text on the card: "Happy New Year" and "Vikram, Sunita, and Meera Bhattachar." We would like to see designs that are very positive in style.

Target Market(s)

The greeting card is going to be sent to family and friends in different parts of the world.

Requirements
Must have
• We would like to have pictures of our daughter Meera on the card. Please find attached 5 photos of her. Please feel free to use all 5 or some of them for the design. We would like the following text on the card: "Happy New Year" and "Vikram, Sunita, and Meera Bhattachar."

```html
<!DOCTYPE html>
<html lang="en">
<head>
<meta charset="utf-8">
<title>Happy New Year 2014 – Meera</title>
<link rel="stylesheet" href="https://fonts.googleapis.com/css2?family=Fredoka:wght@700&family=Arvo:wght@700&family=Great+Vibes&family=Crimson+Text&display=swap">
<style>
  :root {
    --paper: #ffffff;
    --panel-top: #f6f3f8;
    --panel-mid: #c9b8d2;
    --panel-bottom: #6c4f7c;
    --pink: #e27294;
    --digit-blue: #2f6fc4;
    --digit-yellow: #f2c01e;
    --digit-green: #53a83a;
    --digit-magenta: #e0428a;
    --balloon-blue: #7cc3ee;
    --balloon-violet: #b48ad8;
    --text-light: #ffffff;
    --photo-frame: #ffffff;
    --bedding: #f3f1f5;
    --skin: #c99784;
    --blanket: #b6a0d8;
  }
  * { margin: 0; padding: 0; box-sizing: border-box; }
  html, body { width: 1200px; height: 927px; overflow: hidden; background: var(--paper); }
  .card { position: relative; width: 1200px; height: 927px; overflow: hidden; }

  .hero-photo {
    position: absolute; left: 0; top: 0; width: 670px; height: 927px;
    background:
      radial-gradient(ellipse 190px 210px at 310px 300px, var(--skin) 0%, rgba(201,151,132,.85) 45%, rgba(201,151,132,0) 100%),
      radial-gradient(ellipse 520px 420px at 470px 720px, var(--blanket) 0%, #c2b0e0 55%, rgba(194,176,224,0) 100%),
      linear-gradient(150deg, var(--bedding) 0%, #ebe7ee 40%, #e6d8e6 70%, #d9c6de 100%);
  }

  .snapshot {
    position: absolute; background: var(--photo-frame); padding: 10px;
    box-shadow: 0 4px 10px rgba(0,0,0,.35);
  }
  .snapshot .snapshot-image { width: 100%; height: 100%; }
  .snapshot--car-seat { left: 42px; top: 450px; width: 282px; height: 190px; transform: rotate(-10deg); }
  .snapshot--car-seat .snapshot-image { background: linear-gradient(135deg, #3a3a3e, #cfd3da 55%, #f1eef2); }
  .snapshot--blanket { left: 72px; top: 640px; width: 285px; height: 232px; transform: rotate(-8deg); }
  .snapshot--blanket .snapshot-image { background: linear-gradient(160deg, #fbf4ee, #c99a86 50%, #f3d6dc); }
  .snapshot--pink-dress { left: 336px; top: 550px; width: 290px; height: 232px; transform: rotate(5deg); }
  .snapshot--pink-dress .snapshot-image { background: linear-gradient(150deg, #e7e8ea, #8f6a5c 45%, #e7799e); }

  .greeting-panel {
    position: absolute; left: 670px; top: 0; width: 530px; height: 927px;
    background: linear-gradient(180deg, var(--panel-top) 0%, #ece6ef 40%, var(--panel-mid) 70%, var(--panel-bottom) 100%);
  }
  .balloons {
    position: absolute; left: 0; top: 0; width: 530px; height: 300px;
    background:
      radial-gradient(ellipse at 15% 35%, var(--balloon-violet) 0%, transparent 60%),
      radial-gradient(ellipse at 85% 25%, var(--balloon-blue) 0%, transparent 60%),
      linear-gradient(180deg, #8fc9ef 0%, #c7a6dd 55%, rgba(246,243,248,0) 100%);
  }

  .year {
    position: absolute; left: 45px; top: 38px; width: 450px;
    display: flex; justify-content: space-between;
    font-family: "Fredoka", sans-serif; font-weight: 700; font-size: 170px; line-height: 1;
    -webkit-text-stroke: 8px var(--text-light); paint-order: stroke fill;
  }
  .year span { display: inline-block; text-shadow: 0 3px 6px rgba(0,0,0,.25); }
  .year .digit-2 { color: var(--digit-blue); transform: rotate(-4deg); }
  .year .digit-0 { color: var(--digit-yellow); transform: rotate(3deg); }
  .year .digit-1 { color: var(--digit-green); transform: rotate(-3deg); }
  .year .digit-4 { color: var(--digit-magenta); transform: rotate(4deg); }

  .headline {
    position: absolute; left: 0; top: 228px; width: 530px; text-align: center;
    font-family: "Arvo", serif; font-weight: 700; color: var(--pink);
    font-size: 80px; line-height: 82px; letter-spacing: 1px;
    text-shadow: 0 2px 3px rgba(0,0,0,.2);
  }
  .to {
    position: absolute; left: 0; top: 410px; width: 530px; text-align: center;
    font-family: "Arvo", serif; font-weight: 700; color: var(--pink); font-size: 30px;
  }
  .recipient {
    position: absolute; left: 150px; top: 462px; width: 240px; text-align: center;
    font-family: "Great Vibes", cursive; color: var(--text-light); font-size: 80px; line-height: 1;
  }
  .recipient-swash { position: absolute; left: 160px; top: 530px; }

  .sign-off {
    position: absolute; left: 90px; top: 764px; width: 400px; text-align: center;
    font-family: "Crimson Text", serif; color: var(--text-light);
  }
  .sign-off .wishes { font-size: 33px; letter-spacing: .5px; margin-bottom: 6px; }
  .sign-off .family { font-size: 27px; line-height: 36px; }
</style>
</head>
<body>
<main class="card">
  <section class="hero-photo" role="img" aria-label="Main photo of baby Meera lying on white bedding, wrapped in a lavender knitted blanket"></section>

  <figure class="snapshot snapshot--car-seat"><div class="snapshot-image" role="img" aria-label="Photo of Meera asleep in a car seat"></div></figure>
  <figure class="snapshot snapshot--blanket"><div class="snapshot-image" role="img" aria-label="Photo of Meera lying on a soft pink blanket"></div></figure>
  <figure class="snapshot snapshot--pink-dress"><div class="snapshot-image" role="img" aria-label="Photo of Meera smiling in a pink outfit"></div></figure>

  <section class="greeting-panel">
    <div class="balloons" role="img" aria-label="Cluster of blue and purple party balloons"></div>
    <div class="year" aria-label="2014">
      <span class="digit-2">2</span><span class="digit-0">0</span><span class="digit-1">1</span><span class="digit-4">4</span>
    </div>
    <h1 class="headline">HAPPY<br>NEW YEAR</h1>
    <p class="to">to</p>
    <p class="recipient">Meera</p>
    <svg class="recipient-swash" width="210" height="30" viewBox="0 0 210 30" aria-hidden="true">
      <path d="M4 26 C 60 10, 140 4, 206 6" fill="none" stroke="#ffffff" stroke-width="2.5" stroke-linecap="round"/>
    </svg>
    <div class="sign-off">
      <p class="wishes">BEST WISHES</p>
      <p class="family">Vikram, Sunita ,<br>&amp; Meera Bhattachar</p>
    </div>
  </section>
</main>
</body>
</html>
```